Physical Large Banner For Corporate Event

Hi, we would like a large banner designed for a corporate event using adobe illustrator/pdf. The size of the banner must be 2000 (h)x800 (w) mm to fit with the printing requirements (please visit https://www.bannora.com/products/48/banner-stands and see the guidelines for size for a standard banner)

Our organisation holds events for students to find out more on top careers such as Investment Banking & Law. The banner design can be fairly simple but bold using the same themes and colours on our website www.brightpathlearning.co.uk. We can provide imagery of our logo for use/other pictures requested such as those for students/cityscapes etc.

The only text on the banner should be our web address at the bottom (www.brightpathlearning.co.uk) and a line that says "A Head Start in the City, We bring the internship to you..." like in our website homepage.

Target Market(s)

Students & Graduate Recruiters

Industry/Entity Type

Education

Requirements
Must have
• Website address
• Cool imagery
Should not have
• Too much clutter, clean and simple pleaseE

```html
<!DOCTYPE html>
<html lang="en">
<head>
<meta charset="utf-8">
<title>BrightPath – Roll-up Banner Designs</title>
<link rel="stylesheet" href="https://fonts.googleapis.com/css2?family=Marcellus&family=Open+Sans:wght@400;600&display=swap">
<style>
  :root {
    --canvas: #efefef;
    --slate: #5f6064;
    --slate-dark: #4c4d51;
    --white: #ffffff;
    --crimson: #8e1c22;
    --grey-text: #6a6b6f;
    --sky-light: #f7f8fa;
    --tower-blue: #3f4b63;
  }
  * { box-sizing: border-box; margin: 0; padding: 0; }
  html, body { width: 1200px; height: 1119px; overflow: hidden; }
  body {
    background: var(--canvas);
    display: flex;
    justify-content: center;
    align-items: center;
    gap: 45px;
    font-family: "Open Sans", Arial, sans-serif;
  }
  .banner {
    width: 340px;
    height: 850px;
    display: flex;
    flex-direction: column;
    background: var(--white);
    box-shadow: 0 4px 14px rgba(0,0,0,0.12);
  }
  .banner__head {
    height: 330px;
    display: flex;
    flex-direction: column;
    align-items: center;
    padding-top: 44px;
  }
  .brand-dot {
    width: 74px;
    height: 74px;
    border-radius: 50%;
    background: var(--crimson);
  }
  .brand-name {
    margin-top: 30px;
    font-family: "Marcellus", Georgia, serif;
    font-size: 54px;
    line-height: 1;
    letter-spacing: 0.5px;
  }
  .tagline {
    margin-top: 26px;
    font-size: 22px;
    line-height: 1.15;
    text-align: left;
    width: 300px;
  }
  .tagline__sub { display: block; font-size: 16px; margin-top: 2px; }
  .cityscape {
    flex: 1;
    background:
      linear-gradient(100deg, rgba(63,75,99,0.85) 0%, rgba(160,172,190,0.55) 14%, rgba(255,255,255,0) 30%, rgba(255,255,255,0) 66%, rgba(120,132,155,0.6) 80%, rgba(50,60,82,0.9) 100%),
      linear-gradient(180deg, var(--sky-light) 0%, #ffffff 55%, #d9dde5 100%);
  }
  .banner__foot {
    height: 88px;
    display: flex;
    align-items: center;
    justify-content: center;
    gap: 8px;
    font-size: 20px;
  }
  .globe { width: 18px; height: 18px; flex: none; }

  .banner--slate .banner__head { background: var(--slate); color: var(--white); }
  .banner--slate .brand-name { color: var(--white); }
  .banner--slate .banner__foot { background: var(--slate); color: var(--white); }

  .banner--light .banner__head { color: var(--grey-text); }
  .banner--light .brand-name { color: var(--slate-dark); }
  .banner--light .banner__foot { background: var(--slate); color: var(--white); }

  .banner--white .banner__head { color: var(--grey-text); }
  .banner--white .brand-name { color: var(--slate-dark); }
  .banner--white .banner__foot { background: var(--white); color: var(--crimson); }
</style>
</head>
<body>
  <section class="banner banner--slate">
    <header class="banner__head">
      <div class="brand-dot"></div>
      <h1 class="brand-name">BrightPath</h1>
      <p class="tagline">A Head Start in the City<span class="tagline__sub">We bring the internship to you...</span></p>
    </header>
    <div class="cityscape" role="img" aria-label="Photograph looking up between glass skyscrapers towards a bright sky"></div>
    <footer class="banner__foot">
      <svg class="globe" viewBox="0 0 20 20" fill="none" stroke="currentColor" stroke-width="1.6"><circle cx="10" cy="10" r="8.5"/><ellipse cx="10" cy="10" rx="3.8" ry="8.5"/><path d="M1.5 10h17M3 5.5h14M3 14.5h14"/></svg>
      <span>brightpathlearning.co.uk</span>
    </footer>
  </section>

  <section class="banner banner--light">
    <header class="banner__head">
      <div class="brand-dot"></div>
      <h1 class="brand-name">BrightPath</h1>
      <p class="tagline">A Head Start in the City<span class="tagline__sub">We bring the internship to you...</span></p>
    </header>
    <div class="cityscape" role="img" aria-label="Photograph looking up between glass skyscrapers towards a bright sky"></div>
    <footer class="banner__foot">
      <svg class="globe" viewBox="0 0 20 20" fill="none" stroke="currentColor" stroke-width="1.6"><circle cx="10" cy="10" r="8.5"/><ellipse cx="10" cy="10" rx="3.8" ry="8.5"/><path d="M1.5 10h17M3 5.5h14M3 14.5h14"/></svg>
      <span>brightpathlearning.co.uk</span>
    </footer>
  </section>

  <section class="banner banner--white">
    <header class="banner__head">
      <div class="brand-dot"></div>
      <h1 class="brand-name">BrightPath</h1>
      <p class="tagline">A Head Start in the City<span class="tagline__sub">We bring the internship to you...</span></p>
    </header>
    <div class="cityscape" role="img" aria-label="Photograph looking up between glass skyscrapers towards a bright sky"></div>
    <footer class="banner__foot">
      <svg class="globe" viewBox="0 0 20 20" fill="none" stroke="currentColor" stroke-width="1.6"><circle cx="10" cy="10" r="8.5"/><ellipse cx="10" cy="10" rx="3.8" ry="8.5"/><path d="M1.5 10h17M3 5.5h14M3 14.5h14"/></svg>
      <span>brightpathlearning.co.uk</span>
    </footer>
  </section>
</body>
</html>
```